Marketing , Sales and Distribution Website

This website/this business is specifically to start an international marketing, sales and distribution business - no more than 5 pages - one page design with supporting pages, a strong "call to action" design - lead generation design - Modern - can be easily upgraded.

Target Market(s)

Industrial, engineering, Art, technology, food products, fashion and accessories

Industry/Entity Type

Marketing

Coding

Coded - Design and coding required

Font styles to use
Sans Serif

Requirements
Must have
• user friendly. Fast upload time - space for content. Most have strategic "call to action" lead generation opportunities - space for video, links to social media. room for articles, blogs and upcoming tradeshows - modern interactive website - easy to upgrade in the future. Lastly a link or Tab to a one page site dedicated to mobile marketing subscriptions
Nice to have
• Client login area - backend CRM integration - Hubspot
• I am open to suggestions to make this site attractive for companies who import/export goods - or generate leads of companies who wish to import/export their products to the USA - a lot of this information is in the attachment.

```html
<!DOCTYPE html>
<html lang="en">
<head>
<meta charset="utf-8">
<title>Corvane Marketing</title>
<link rel="stylesheet" href="https://fonts.googleapis.com/css2?family=Roboto:wght@300;400;500;700&display=swap">
<style>
:root{
  --navy:#26387a;
  --navy-deep:#1f2f68;
  --navy-text:#23336e;
  --sky:#9bb5dd;
  --sky-line:#b7cae8;
  --ink:#555b66;
  --muted:#7a808a;
  --white:#ffffff;
  --rule:#e4e7ee;
}
*{box-sizing:border-box;margin:0;padding:0}
html,body{width:1200px;height:3180px;overflow:hidden}
body{font-family:"Roboto",Arial,sans-serif;color:var(--ink);background:var(--white);position:relative}
.abs{position:absolute}
a{color:inherit;text-decoration:none}

/* header */
.site-header{position:absolute;left:0;top:0;width:1200px;height:120px;background:var(--white);z-index:5}
.brand{position:absolute;left:100px;top:0;width:204px;height:204px;border-radius:50%;background:var(--navy);border:6px solid var(--white);display:flex;align-items:center;justify-content:center;z-index:6}
.brand-name{color:var(--white);font-weight:700;font-size:30px;letter-spacing:1px}
.main-nav{position:absolute;top:52px;left:483px;display:flex;gap:0}
.main-nav a{font-size:14px;color:#4a4f5a;margin-right:36px;text-transform:uppercase;letter-spacing:.3px;padding-bottom:10px}
.main-nav a.is-active{color:var(--navy-text);font-weight:500;border-bottom:2px solid var(--navy)}

/* hero */
.hero{position:absolute;left:0;top:120px;width:1200px;height:600px;background:linear-gradient(135deg,#3a5590 0%,#6a86b8 35%,#4d6aa2 60%,#23386e 100%)}
.hero-curve{position:absolute;left:0;bottom:0;width:1200px;height:70px}
.hero-title{position:absolute;top:176px;width:100%;text-align:center;color:var(--white);font-size:40px;font-weight:500;letter-spacing:1px}
.hero-sub{position:absolute;top:228px;width:100%;text-align:center;color:var(--white);font-size:22px;font-weight:300}
.hero-btn{position:absolute;left:505px;top:291px;width:190px;height:47px;background:#8eaee0;color:var(--white);font-size:18px;display:flex;align-items:center;justify-content:center;text-transform:uppercase;letter-spacing:.5px}
.slider-dots{position:absolute;top:500px;left:572px;display:flex;gap:4px}
.slider-dots span{width:16px;height:16px;border-radius:50%;background:var(--white)}
.slider-dots span.is-current{background:transparent;border:2px solid var(--white)}

/* section titles */
.section-title{position:absolute;width:100%;text-align:center;font-size:42px;font-weight:300;color:#2a2f3a}
.section-title em{font-style:normal;color:var(--navy-text)}

/* welcome */
.welcome-intro{position:absolute;top:800px;left:190px;width:820px;text-align:center;font-size:16px;line-height:30px;color:var(--ink)}
.welcome-rule{position:absolute;top:890px;left:190px;width:820px;height:1px;background:var(--rule)}
.service{position:absolute;top:935px;width:300px;text-align:center}
.service-icon{width:148px;height:148px;border-radius:50%;background:var(--navy);margin:0 auto;display:flex;align-items:center;justify-content:center}
.service-name{margin-top:12px;font-size:22px;color:#2a2f3a;text-transform:uppercase;letter-spacing:.5px}
.service-text{margin-top:8px;font-size:15px;line-height:24px;color:var(--ink)}
.outline-btn{display:inline-flex;align-items:center;justify-content:center;border:2px solid var(--navy);color:var(--navy-text);font-size:16px;text-transform:uppercase;background:var(--white)}
.service .outline-btn{margin-top:34px;width:154px;height:44px}

/* about */
.about{position:absolute;left:0;top:1318px;width:1200px;height:440px;background:linear-gradient(120deg,#2f4587 0%,#4a63a4 40%,#3c5596 70%,#24387a 100%)}
.about-title{position:absolute;top:62px;width:100%;text-align:center;color:var(--white);font-size:44px;font-weight:400}
.about-text{position:absolute;left:160px;width:880px;text-align:center;color:var(--white);font-size:17px;line-height:30px}
.about-btn{position:absolute;left:452px;top:303px;width:296px;height:50px;border:2px solid rgba(255,255,255,.85);color:var(--white);font-size:15px;display:flex;align-items:center;justify-content:center;text-transform:uppercase}

/* video */
.video-copy{position:absolute;left:100px;top:1915px;width:540px;font-size:14px;line-height:26px;color:var(--ink)}
.video-copy p+p{margin-top:18px}
.more-btn{position:absolute;left:100px;top:2141px;width:236px;height:50px;font-size:15px;gap:10px}
.video-frame{position:absolute;left:668px;top:1908px;width:436px;height:278px;background:var(--white);border:1px solid #dde1e8;box-shadow:0 2px 6px rgba(0,0,0,.15);padding:12px}
.video-poster{position:relative;width:410px;height:226px;background:linear-gradient(135deg,#c9ccd0 0%,#e9eaec 45%,#9da2a9 100%)}
.video-play{position:absolute;left:175px;top:83px}
.video-bar{width:410px;height:28px;background:#2b2e34;display:flex;align-items:center;padding:0 12px;gap:14px}
.video-track{flex:1;height:5px;background:#d9dbe0;position:relative}
.video-track::before{content:"";position:absolute;left:0;top:0;width:38%;height:5px;background:#5b8fd4}

/* news band */
.news-band{position:absolute;left:0;top:2260px;width:1200px;height:582px;background:var(--sky)}
.band-title{position:absolute;top:62px;font-size:30px;color:var(--navy-text);font-weight:400}
.band-divider{position:absolute;left:450px;top:60px;width:1px;height:470px;background:var(--sky-line)}
.article-photo{position:absolute;left:100px;top:131px;width:292px;height:174px;background:linear-gradient(135deg,#f3f3f1 0%,#7b6f63 40%,#4d4540 75%,#e6e6e6 100%);border:3px solid var(--white)}
.article-text{position:absolute;left:100px;top:322px;width:300px;color:var(--white);font-size:13px;line-height:22px}
.ghost-btn{position:absolute;left:100px;top:462px;width:126px;height:40px;border:2px solid var(--white);color:var(--white);font-size:15px;display:flex;align-items:center;justify-content:center}
.show{position:absolute;left:478px;width:340px;height:110px}
.show-date{position:absolute;left:0;top:0;width:104px;height:104px;border-radius:50%;border:1px solid rgba(255,255,255,.75);color:var(--white);text-align:center}
.show-day{display:block;margin-top:14px;font-size:44px;font-weight:300;line-height:48px}
.show-month{display:block;font-size:11px;letter-spacing:.5px}
.show-name{position:absolute;left:120px;top:8px;font-size:14px;font-weight:500;color:var(--white);text-transform:uppercase}
.show-text{position:absolute;left:120px;top:32px;width:210px;font-size:12px;line-height:19px;color:var(--white)}
.blog-photo{position:absolute;left:880px;width:202px;height:108px;border:3px solid var(--white)}
.blog-photo.team{background:linear-gradient(135deg,#e7ecf2 0%,#6b7585 45%,#2e3440 80%,#cfd6de 100%)}
.blog-photo.chart{background:linear-gradient(135deg,#f4f6f3 0%,#c9dba8 40%,#e4eef6 70%,#b9c4cf 100%)}
.blog-name{position:absolute;left:880px;font-size:12px;font-weight:500;color:var(--white);text-transform:uppercase}
.blog-text{position:absolute;left:880px;width:210px;font-size:11.5px;line-height:17px;color:var(--white)}

/* footer */
.site-footer{position:absolute;left:0;top:2842px;width:1200px;height:268px;background:var(--navy)}
.foot-col{position:absolute;top:40px;color:var(--white)}
.foot-head{font-size:14px;font-weight:700;text-transform:uppercase;letter-spacing:.3px;margin-bottom:18px}
.foot-list{list-style:none;font-size:11.5px;line-height:27.5px}
.news-text{font-size:11.5px;line-height:20px;width:250px}
.news-input{margin-top:20px;width:243px;height:40px;background:var(--white);color:#9aa0aa;font-size:12px;display:flex;align-items:center;padding-left:14px}
.news-btn{margin-top:14px;width:90px;height:40px;background:#8eaee0;color:var(--white);font-size:12px;display:flex;align-items:center;justify-content:center;text-transform:uppercase}
.contact-line{display:flex;align-items:center;gap:10px;font-size:11.5px;line-height:27px}
.legal-bar{position:absolute;left:0;top:3110px;width:1200px;height:70px;background:var(--navy-deep);color:var(--white);font-size:11.5px}
.legal-copy{position:absolute;left:100px;top:28px}
.social{position:absolute;left:778px;top:27px;display:flex;align-items:center;gap:18px}
.social i{display:block;width:11px;height:11px;border-radius:50%;background:var(--white)}
</style>
</head>
<body>

<header class="site-header">
  <nav class="main-nav">
    <a href="#" class="is-active">Home</a>
    <a href="#">About us</a>
    <a href="#">Services</a>
    <a href="#">Careers</a>
    <a href="#">Blog</a>
    <a href="#">News</a>
    <a href="#">Contact</a>
  </nav>
</header>
<div class="brand"><span class="brand-name">CORVANE</span></div>

<section class="hero" role="img" aria-label="Businessman in a suit touching a transparent screen of charts, graphs and a world map">
  <h1 class="hero-title">CORVANE MARKETING</h1>
  <p class="hero-sub">We are an international marketing, sales and distribution business</p>
  <a href="#" class="hero-btn">Get in touch</a>
  <div class="slider-dots"><span class="is-current"></span><span></span><span></span></div>
  <svg class="hero-curve" viewBox="0 0 1200 70" preserveAspectRatio="none"><path d="M0 70 L0 44 Q600 -36 1200 44 L1200 70 Z" fill="#ffffff"/></svg>
</section>

<h2 class="section-title" style="top:740px">Welcome to <em>Corvane</em></h2>
<p class="welcome-intro">Sed do eiusmod tempor incididunt ut labore et dolore magna aliqua. Ut enim ad minim veniam, quis nostrud exercitation ullamco laboris nisi.</p>
<div class="welcome-rule"></div>

<div class="service" style="left:90px">
  <div class="service-icon">
    <svg width="76" height="70" viewBox="0 0 76 70" fill="#fff"><rect x="6" y="46" width="10" height="20"/><rect x="22" y="38" width="10" height="28"/><rect x="38" y="30" width="10" height="36"/><rect x="54" y="22" width="10" height="44"/><path d="M2 40 L30 18 L40 26 L60 8 L54 4 L72 0 L68 18 L63 12 L40 34 L30 26 L6 46 Z"/></svg>
  </div>
  <h3 class="service-name">Marketing</h3>
  <p class="service-text">Sed ut perspiciatis unde omnis iste natus error sit voluptatem accusantium.</p>
  <a href="#" class="outline-btn">Read more</a>
</div>
<div class="service" style="left:450px">
  <div class="service-icon">
    <svg width="84" height="56" viewBox="0 0 84 56" fill="#fff"><path d="M0 10 L14 6 L24 34 L10 38 Z"/><path d="M84 10 L70 6 L60 34 L74 38 Z"/><path d="M22 12 L38 8 L50 14 L62 10 L66 30 L50 46 Q44 52 38 46 L26 36 Z"/></svg>
  </div>
  <h3 class="service-name">Sales</h3>
  <p class="service-text">Sed ut perspiciatis unde omnis iste natus error sit voluptatem accusantium.</p>
  <a href="#" class="outline-btn">Read more</a>
</div>
<div class="service" style="left:808px">
  <div class="service-icon">
    <svg width="76" height="70" viewBox="0 0 76 70" fill="#fff"><rect x="6" y="24" width="12" height="22"/><path d="M18 24 L50 6 L50 64 L18 46 Z"/><path d="M22 48 L32 48 L36 66 L28 66 Z"/><path d="M58 24 L70 16 L72 20 L60 28 Z"/><path d="M60 34 L74 34 L74 38 L60 38 Z"/><path d="M58 46 L72 54 L70 58 L56 50 Z"/></svg>
  </div>
  <h3 class="service-name">Distribution</h3>
  <p class="service-text">Sed ut perspiciatis unde omnis iste natus error sit voluptatem accusantium.</p>
  <a href="#" class="outline-btn">Read more</a>
</div>

<section class="about" role="img" aria-label="Business people standing in a bright modern office, tinted blue">
  <h2 class="about-title">About Corvane</h2>
  <p class="about-text" style="top:134px">But I must explain to you how all this mistaken idea of denouncing pleasure and praising pain was born and I will give you a complete account of the system.</p>
  <p class="about-text" style="top:212px">At vero eos et accusamus et iusto odio dignissimos ducimus qui blanditiis praesentium voluptatum deleniti atque corrupti quos dolores et quas molestias excepturi sint occaecati cupiditate.</p>
  <a href="#" class="about-btn">Lead generation opportunities</a>
</section>

<h2 class="section-title" style="top:1808px">Our <em>Video</em></h2>
<div class="video-copy">
  <p>Sed ut perspiciatis unde omnis iste natus error sit voluptatem accusantium doloremque laudantium, totam rem aperiam, eaque ipsa quae ab illo inventore veritatis et quasi architecto beatae vitae dicta sunt explicabo.</p>
  <p>Ut enim ad minim veniam, quis nostrud exercitation ullamco laboris nisi ut aliquip ex ea commodo consequat. Duis aute irure dolor in reprehenderit in voluptate velit esse cillum dolore eu fugiat nulla pariatur. Excepteur sint occaecat cupidatat non proident.</p>
</div>
<a href="#" class="outline-btn more-btn">More information
  <svg width="8" height="12" viewBox="0 0 8 12"><path d="M1 1 L6 6 L1 11" stroke="#26387a" stroke-width="2" fill="none"/></svg></a>
<div class="video-frame">
  <div class="video-poster" role="img" aria-label="Hands of colleagues pointing at paper charts on a meeting table">
    <svg class="video-play" width="62" height="62" viewBox="0 0 62 62"><circle cx="31" cy="31" r="28" fill="none" stroke="#fff" stroke-width="3"/><path d="M24 18 L46 31 L24 44 Z" fill="#fff"/></svg>
  </div>
  <div class="video-bar">
    <svg width="10" height="12" viewBox="0 0 10 12"><path d="M0 0 L10 6 L0 12 Z" fill="#fff"/></svg>
    <div class="video-track"></div>
    <svg width="14" height="12" viewBox="0 0 14 12"><path d="M0 4 H3 L7 0 V12 L3 8 H0 Z" fill="#fff"/><path d="M9 3 Q12 6 9 9" stroke="#fff" stroke-width="1.5" fill="none"/></svg>
  </div>
</div>

<section class="news-band">
  <h2 class="band-title" style="left:100px">Articles</h2>
  <div class="article-photo" role="img" aria-label="Laptop, coffee cup and notebook on a wooden desk, seen from above"></div>
  <p class="article-text">Praesent a accumsan est. Nam ornare erat sed tortor iaculis posuere. Suspendisse tempus luctus nunc, ut laoreet leo. Nam neque tellus, ornare vitae lobortis id, sagittis vitae arcu. Maecenas a adipiscing nisl. Nullam sed risus sit amet ipsum lobortis condimentum.</p>
  <a href="#" class="ghost-btn">Read More ›</a>

  <div class="band-divider"></div>

  <h2 class="band-title" style="left:490px">Upcoming Tradeshows</h2>
  <div class="show" style="top:128px">
    <div class="show-date"><span class="show-day">09</span><span class="show-month">JAN / 2017</span></div>
    <h3 class="show-name">Nostrud exercitation</h3>
    <p class="show-text">Suspendisse tempus luctus nunc, ut laoreet leo. Nam neque tellus, ornare vitae lobortis.</p>
  </div>
  <div class="show" style="top:264px">
    <div class="show-date"><span class="show-day">04</span><span class="show-month">FEB / 2017</span></div>
    <h3 class="show-name">Unde omnis iste natus</h3>
    <p class="show-text">Suspendisse tempus luctus nunc, ut laoreet leo. Nam neque tellus, ornare vitae lobortis.</p>
  </div>
  <div class="show" style="top:400px">
    <div class="show-date"><span class="show-day">15</span><span class="show-month">JAN / 2017</span></div>
    <h3 class="show-name">Officia deserunt mollit</h3>
    <p class="show-text">Suspendisse tempus luctus nunc, ut laoreet leo. Nam neque tellus, ornare vitae lobortis.</p>
  </div>

  <h2 class="band-title" style="left:876px">Our Blogs</h2>
  <div class="blog-photo team" style="top:131px" role="img" aria-label="Business team seated around a meeting table"></div>
  <h3 class="blog-name" style="top:252px">Praesent a accumsan est</h3>
  <p class="blog-text" style="top:270px">At vero eos et accusamus et iusto odio dignissimos ducimus qui blanditiis</p>
  <div class="blog-photo chart" style="top:330px" role="img" aria-label="Hand with a pen reviewing printed bar charts"></div>
  <h3 class="blog-name" style="top:450px">Mauris fermentum magna</h3>
  <p class="blog-text" style="top:468px">Donec sit amet eros. Lorem ipsum dolor sit amet consectetuer adipiscing elit.</p>
</section>

<footer class="site-footer">
  <div class="foot-col" style="left:100px">
    <h4 class="foot-head">Links</h4>
    <ul class="foot-list"><li>Home</li><li>About us</li><li>Services</li><li>Careers</li><li>Blog</li><li>Articles</li></ul>
  </div>
  <div class="foot-col" style="left:252px">
    <h4 class="foot-head">Join our newsletter</h4>
    <p class="news-text">Excepteur sint occaecat cupidatat non proident, sunt in culpa qui</p>
    <div class="news-input">Enter Your Email</div>
    <div class="news-btn">Subscribe</div>
  </div>
  <div class="foot-col" style="left:589px">
    <h4 class="foot-head">Information</h4>
    <ul class="foot-list"><li>Terms &amp; Conditions</li><li>Privacy policy</li><li>Disclaimer</li><li>Contact us</li><li>Sitemap</li></ul>
  </div>
  <div class="foot-col" style="left:786px">
    <h4 class="foot-head">Why us</h4>
    <ul class="foot-list"><li>Customers</li><li>Team</li><li>FAQ</li><li>News</li><li>Others</li></ul>
  </div>
  <div class="foot-col" style="left:954px">
    <h4 class="foot-head">Contact info</h4>
    <ul class="foot-list"><li><strong>Corvane</strong></li><li>NO, Street Name,</li><li>City Name, Country.</li></ul>
    <div class="contact-line"><svg width="12" height="12" viewBox="0 0 12 12"><path d="M2 0 L4.5 0 L5.5 3 L4 4.5 Q5 7 7.5 8 L9 6.5 L12 7.5 L12 10 Q12 12 10 12 Q0 11 0 2 Q0 0 2 0 Z" fill="#fff"/></svg>+11 (0) 555 014 27</div>
    <div class="contact-line"><svg width="12" height="10" viewBox="0 0 12 10"><rect width="12" height="10" fill="#fff"/><path d="M0 0 L6 5 L12 0" stroke="#26387a" fill="none"/></svg>hello@corvanetrade.com</div>
  </div>
</footer>
<div class="legal-bar">
  <span class="legal-copy">© 2017. Corvane. All rights reserved</span>
  <div class="social"><span>Connect with our social network :</span><i></i><i></i><i></i><i></i><i></i></div>
</div>

</body>
</html>
```